Wattlebrook Lather Co needs packaging for Bars of Soap

I need a design for packaging bars of soap. My soaps are focused on quality ingredients, utilising Australian Clay's and unique Australian essential oils. The Soaps are designed to benefit the skin by lightly exfoliating, cleansing while moisturizing and softening the skin.

I am wanting a soap box designed.
The box should be 95mm x 70mm x 28mm
Have an upmarket quality feel.
I am thinking of using grey, but am open to other natural colours.
The box will have the logo, web address, space left so I can add the ingredient list.
The text 'Handcrafted in Merrigan Bay' on the box. (If it fits comfortably)

Target Market(s)

25-50yrs , health and body conscious

Industry/Entity Type

Health And Wellness

Requirements
Must have
• include the web address.
• space for the scent/type of clay for each soap. This will change, as will the ingredients as I create new soaps. I would like the ability to change this as required easily myself if possible?
Nice to have
• I am swaying towards grey but am not locked in to it.
• Handcrafted in Merrigan Bay (text added on the box)

```html
<!DOCTYPE html>
<html lang="en">
<head>
<meta charset="utf-8">
<title>Wattlebrook Lather Co – Soap Box Packaging</title>
<link href="https://fonts.googleapis.com/css2?family=Amatic+SC:wght@700&family=Reenie+Beanie&display=swap" rel="stylesheet">
<style>
  :root {
    --page: #ffffff;
    --slate-dark: #3e3e3e;
    --slate-mid: #5c5c5c;
    --slate-light: #6f6f6f;
    --label-grey: #cbcccd;
    --ink: #4a4a4c;
    --wattle: #f9c55a;
    --wattle-soft: rgba(249, 210, 130, 0.55);
    --line-grey: #9a9a9a;
  }
  * { box-sizing: border-box; margin: 0; padding: 0; }
  html, body { width: 1200px; height: 1000px; overflow: hidden; background: var(--page); }
  .canvas { position: relative; width: 1200px; height: 1000px; }

  .box-face {
    position: absolute;
    background: linear-gradient(135deg, var(--slate-dark) 0%, var(--slate-mid) 45%, var(--slate-light) 100%);
    overflow: hidden;
  }
  .box-face--front { left: 118px; top: 388px; width: 517px; height: 309px; }
  .box-face--preview { left: 740px; top: 116px; width: 342px; height: 206px; }

  .botanical {
    position: absolute;
    border-radius: 46% 54% 40% 60% / 50% 42% 58% 50%;
    background: radial-gradient(ellipse at 60% 40%, var(--wattle-soft) 0%, rgba(200,200,200,0.35) 45%, rgba(120,120,120,0.12) 75%, rgba(255,255,255,0) 100%);
  }
  .botanical--front { left: 280px; top: 290px; width: 560px; height: 605px; }
  .botanical--preview { left: 870px; top: 116px; width: 212px; height: 206px; border-radius: 40%; }

  .label {
    position: absolute;
    background: var(--label-grey);
    text-align: center;
    color: var(--ink);
  }
  .label__spine {
    position: absolute;
    background: var(--wattle);
  }
  .label__web {
    position: absolute;
    font-family: "Reenie Beanie", cursive;
    color: var(--ink);
    transform: rotate(-90deg);
    white-space: nowrap;
  }
  .label__name {
    font-family: "Amatic SC", sans-serif;
    font-weight: 700;
    line-height: 1;
    color: var(--ink);
  }
  .label__origin {
    font-family: "Reenie Beanie", cursive;
    color: var(--ink);
  }
  .label__wave { display: block; margin: 0 auto; }
  .label__note {
    font-family: "Amatic SC", sans-serif;
    font-weight: 700;
    color: var(--ink);
    letter-spacing: 0.5px;
  }

  /* front label */
  .label--front { left: 130px; top: 458px; width: 313px; height: 174px; padding-top: 12px; }
  .label__spine--front { left: 114px; top: 458px; width: 16px; height: 174px; }
  .label__web--front { left: 60px; top: 536px; width: 140px; font-size: 13px; text-align: center; }
  .label--front .label__name { font-size: 46px; padding: 0 14px; }
  .label--front .label__origin { font-size: 20px; margin-top: 6px; }
  .label--front .label__note { font-size: 11px; margin-top: 2px; }

  /* preview label */
  .label--preview { left: 746px; top: 163px; width: 209px; height: 116px; padding-top: 8px; }
  .label__spine--preview { left: 737px; top: 163px; width: 9px; height: 116px; }
  .label__web--preview { left: 697px; top: 214px; width: 100px; font-size: 9px; text-align: center; }
  .label--preview .label__name { font-size: 30px; padding: 0 10px; }
  .label--preview .label__origin { font-size: 13px; margin-top: 4px; }
  .label--preview .label__note { font-size: 7px; }
</style>
</head>
<body>
<main class="canvas">

  <!-- front panel -->
  <div class="box-face box-face--front" role="img" aria-label="Dark grey clay stone texture"></div>
  <div class="label__spine label__spine--front"></div>
  <div class="label label--front">
    <div class="label__name">Wattlebrook Lather Co</div>
    <div class="label__origin">Handcrafted in Merrigan Bay</div>
    <svg class="label__wave" width="60" height="6" viewBox="0 0 60 6" aria-hidden="true">
      <path d="M0 3 Q3 0 6 3 T12 3 T18 3 T24 3 T30 3 T36 3 T42 3 T48 3 T54 3 T60 3" fill="none" stroke="var(--line-grey)" stroke-width="1"/>
    </svg>
    <div class="label__note">Made with Australian clay &amp; essential oils</div>
  </div>
  <div class="label__web label__web--front">www.wattlebrooklather.com.au</div>
  <div class="botanical botanical--front" role="img" aria-label="Line drawing of a wattle flower branch with leaves and soft yellow blooms"></div>

  <!-- preview panel -->
  <div class="box-face box-face--preview" role="img" aria-label="Dark grey clay stone texture"></div>
  <div class="botanical botanical--preview" role="img" aria-label="Line drawing of wattle flowers with soft yellow blooms"></div>
  <div class="label__spine label__spine--preview"></div>
  <div class="label label--preview">
    <div class="label__name">Wattlebrook Lather Co</div>
    <div class="label__origin">Handcrafted in Merrigan Bay</div>
    <svg class="label__wave" width="40" height="5" viewBox="0 0 40 5" aria-hidden="true">
      <path d="M0 2.5 Q2.5 0 5 2.5 T10 2.5 T15 2.5 T20 2.5 T25 2.5 T30 2.5 T35 2.5 T40 2.5" fill="none" stroke="var(--line-grey)" stroke-width="0.8"/>
    </svg>
    <div class="label__note">Made with Australian clay &amp; essential oils</div>
  </div>
  <div class="label__web label__web--preview">www.wattlebrooklather.com.au</div>

</main>
</body>
</html>
```